Business Cards using attached files

Please make new business cards using files attached. I would like something a little more updated possibly. Double sided.
I am wanting to make sure I can change the names and positions easily myself.

Target Market(s)

Automotive Repair

Industry/Entity Type

Automotive

Contact Information for Business Card

See attached files

Font styles to use
Serif

Colors
0054AA
0677BA
7BADD7
CADEEF
E8F1F8

Requirements
Must have
• Red white blue colors
Nice to have
• I'd like it slightly updated from our existing design. Double sided. I'd like to be able to change names and positions easily to have them printed.
Should not have
• I'm not sure

```html
<!DOCTYPE html>
<html lang="en">
<head>
<meta charset="utf-8">
<title>Keystone Auto &amp; Truck – Business Card</title>
<link rel="stylesheet" href="https://fonts.googleapis.com/css2?family=Tinos:ital,wght@0,400;0,700;1,400;1,700&display=swap">
<style>
  :root {
    --red: #c8242b;
    --red-dark: #8e2a3a;
    --navy: #1f3a5f;
    --ink: #2b2b2b;
    --paper: #ffffff;
    --paper-shade: #ececec;
    --backdrop: #3a3a3c;
    --social-blue: #3b5ea8;
    --social-sky: #1d9bd8;
  }
  * { box-sizing: border-box; margin: 0; padding: 0; }
  html, body { width: 1200px; height: 900px; overflow: hidden; }
  body {
    background: var(--backdrop);
    font-family: "Tinos", "Times New Roman", serif;
    color: var(--ink);
    position: relative;
  }
  .card {
    position: absolute;
    left: 250px;
    width: 700px;
    height: 400px;
    background: linear-gradient(120deg, var(--paper-shade) 0%, var(--paper) 45%, var(--paper) 70%, var(--paper-shade) 100%);
    overflow: hidden;
    box-shadow: 0 10px 24px rgba(0,0,0,.45);
  }
  .card--back { top: 35px; }
  .card--front { top: 465px; }
  .card__wedges { position: absolute; inset: 0; width: 100%; height: 100%; }

  /* brand mark */
  .brand { position: absolute; display: flex; align-items: center; gap: 10px; white-space: nowrap; }
  .brand__dot { border: 4px solid var(--navy); border-radius: 50%; flex: none; }
  .brand__name { font-weight: 700; color: var(--navy); letter-spacing: 1px; }

  /* back side */
  .card--back .brand { top: 48px; right: 110px; }
  .card--back .brand__dot { width: 34px; height: 34px; }
  .card--back .brand__name { font-size: 34px; }
  .online { position: absolute; top: 132px; right: 92px; text-align: right; }
  .online__title { color: var(--red); font-weight: 700; font-size: 17px; }
  .online__url { font-size: 15px; color: var(--ink); }
  .online__icons { display: flex; gap: 10px; justify-content: flex-end; margin-top: 8px; }
  .online__icons span { width: 26px; height: 26px; border-radius: 50%; }
  .online__icons .is-blue { background: var(--social-blue); }
  .online__icons .is-sky { background: var(--social-sky); }
  .online__icons .is-ring { border: 2px solid #cfcfcf; background: #fff; }

  .promise { position: absolute; left: 120px; top: 150px; }
  .promise__title { color: var(--red); font-weight: 700; font-size: 19px; margin-bottom: 4px; }
  .promise__list { list-style: none; }
  .promise__list li { font-size: 17px; line-height: 25px; padding-left: 26px; position: relative; }
  .promise__list li::before {
    content: ""; position: absolute; left: 4px; top: 6px;
    width: 6px; height: 11px;
    border: solid var(--red); border-width: 0 3px 3px 0;
    transform: rotate(40deg);
  }

  /* front side */
  .card--front .brand { left: 40px; top: 172px; }
  .card--front .brand__dot { width: 32px; height: 32px; }
  .card--front .brand__name { font-size: 30px; }
  .divider { position: absolute; left: 305px; top: 120px; width: 2px; height: 230px; background: var(--navy); }
  .person { position: absolute; left: 335px; top: 78px; }
  .person__name { color: var(--red); font-weight: 700; font-size: 25px; letter-spacing: 1px; text-transform: uppercase; }
  .person__role { font-size: 16px; color: #555; }
  .contact { position: absolute; left: 335px; top: 150px; list-style: none; }
  .contact__group { margin-bottom: 8px; }
  .contact__row { display: flex; align-items: center; gap: 8px; font-size: 15px; line-height: 19px; }
  .contact__row svg { width: 14px; height: 14px; flex: none; fill: var(--red); }
  .contact__row .spacer { width: 14px; flex: none; }
  .tagline { position: absolute; left: 335px; top: 300px; color: var(--navy); }
  .tagline__lead { font-style: italic; font-size: 15px; }
  .tagline__services { font-style: italic; font-weight: 700; font-size: 15px; line-height: 20px; }
</style>
</head>
<body>

  <section class="card card--back" aria-label="Business card, back side">
    <svg class="card__wedges" viewBox="0 0 700 400" preserveAspectRatio="none" aria-hidden="true">
      <defs>
        <linearGradient id="wedgeRed" x1="0" y1="0" x2="1" y2="1">
          <stop offset="0" stop-color="#d02a2f"/>
          <stop offset="1" stop-color="#8e2a3a"/>
        </linearGradient>
      </defs>
      <path d="M0 0 H190 Q50 130 0 320 Z" fill="url(#wedgeRed)"/>
      <path d="M190 0 Q50 130 0 320" fill="none" stroke="var(--navy)" stroke-width="4"/>
      <path d="M700 110 V400 H470 Q640 300 700 110 Z" fill="url(#wedgeRed)"/>
      <path d="M700 110 Q640 300 470 400" fill="none" stroke="var(--navy)" stroke-width="4"/>
    </svg>

    <div class="brand">
      <span class="brand__dot"></span>
      <span class="brand__name">KEYSTONE</span>
    </div>

    <div class="online">
      <p class="online__title">Find Us Online:</p>
      <p class="online__url">www.keystoneautotruck.com</p>
      <div class="online__icons">
        <span class="is-blue"></span><span class="is-sky"></span><span class="is-ring"></span>
      </div>
    </div>

    <div class="promise">
      <p class="promise__title">We Stand Behind Our Service</p>
      <ul class="promise__list">
        <li>Family Owned &amp; Operated</li>
        <li>Complimentary 2 year/24,000 mile warranty</li>
        <li>Free local pickup/dropoff service</li>
        <li>Experts In Domestic &amp; Import Service</li>
        <li>Master Certified Mechanics</li>
        <li>Diesel &amp; Fleet Services Available</li>
        <li>Honest, Knowledgeable, Trustworthy Service</li>
        <li>Top Rated A+ Auto Repair Facility</li>
      </ul>
    </div>
  </section>

  <section class="card card--front" aria-label="Business card, front side">
    <svg class="card__wedges" viewBox="0 0 700 400" preserveAspectRatio="none" aria-hidden="true">
      <defs>
        <linearGradient id="wedgeRed2" x1="0" y1="0" x2="1" y2="1">
          <stop offset="0" stop-color="#d02a2f"/>
          <stop offset="1" stop-color="#8e2a3a"/>
        </linearGradient>
      </defs>
      <path d="M360 0 H700 V150 Q610 30 360 0 Z" fill="url(#wedgeRed2)"/>
      <path d="M360 0 Q610 30 700 150" fill="none" stroke="var(--navy)" stroke-width="4"/>
      <path d="M0 250 Q130 360 340 400 H0 Z" fill="url(#wedgeRed2)"/>
      <path d="M0 250 Q130 360 340 400" fill="none" stroke="var(--navy)" stroke-width="4"/>
    </svg>

    <div class="brand">
      <span class="brand__dot"></span>
      <span class="brand__name">KEYSTONE</span>
    </div>

    <div class="divider"></div>

    <div class="person">
      <p class="person__name">Daniel Marsh</p>
      <p class="person__role">General Manager</p>
    </div>

    <ul class="contact">
      <li class="contact__group">
        <div class="contact__row">
          <svg viewBox="0 0 16 16"><path d="M3 1l3 3-2 2c1 2 3 4 5 5l2-2 3 3-2 3C6 15 1 10 1 3z"/></svg>
          <span>(555) 014-2280</span>
        </div>
        <div class="contact__row">
          <svg viewBox="0 0 16 16"><rect x="4" y="1" width="8" height="5"/><rect x="1" y="6" width="14" height="6" rx="1"/><rect x="4" y="12" width="8" height="3"/></svg>
          <span>(555) 014-3391</span>
        </div>
      </li>
      <li class="contact__group">
        <div class="contact__row">
          <svg viewBox="0 0 16 16"><path d="M1 3h14v10H1z M1 3l7 6 7-6" stroke="#fff" stroke-width="1"/></svg>
          <span>dan@keystoneautotruck.com</span>
        </div>
        <div class="contact__row">
          <svg viewBox="0 0 16 16"><circle cx="8" cy="8" r="7"/><path d="M1 8h14M8 1c-3 4-3 10 0 14M8 1c3 4 3 10 0 14" stroke="#fff" fill="none"/></svg>
          <span>www.keystoneautotruck.com</span>
        </div>
      </li>
      <li class="contact__group">
        <div class="contact__row">
          <svg viewBox="0 0 16 16"><path d="M8 0a5 5 0 0 1 5 5c0 4-5 11-5 11S3 9 3 5a5 5 0 0 1 5-5z"/><circle cx="8" cy="5" r="2" fill="#fff"/></svg>
          <span>48 Mill Road</span>
        </div>
        <div class="contact__row">
          <span class="spacer"></span>
          <span>Brookfield, NY 10020</span>
        </div>
      </li>
    </ul>

    <div class="tagline">
      <p class="tagline__lead">Family Owned &amp; Operated Since 1991</p>
      <p class="tagline__services">Auto Service - Inspections - Lube/Oil Service</p>
      <p class="tagline__services">Diesel - Fleet - DOT - Truck - Trailer</p>
    </div>
  </section>

</body>
</html>
```